New Optometry Practice needs a Business Card

Need a business card for an Optometry practice called 'Marlow Vista Eyecare'. I would like to use designs that are friendly, fun and professional. Looking to incorporate glasses (see uploaded image). Not interested in design with an 'eye' in logo. Like green, blue, white as color choices..but open to your ideas. Back of card will be an appointment card as well as provide address, phone and email information.

Industry/Entity Type

Business

Contact Information for Business Card

Marlow Vista Eyecare
Dr. Petra Lindqvist, Optometrist (or O.D.)
4172 S Corbell Ave Wenatchee, WA 98736
PMarlowvistaeyecare.example

Colors
acd036
33b8a4
f68d4e
cfeae6
fee18a
cadf82

Requirements
Must have
• Appointment card on back with date/time of return for next exam

```html
<!DOCTYPE html>
<html lang="en">
<head>
<meta charset="utf-8">
<title>Marlow Vista Eyecare – Business Card</title>
<link rel="stylesheet" href="https://fonts.googleapis.com/css2?family=Open+Sans:ital,wght@0,400;0,600;0,700;1,400&display=swap">
<style>
  :root {
    --backdrop: #e6e7ea;
    --card: #ffffff;
    --navy: #1f2e78;
    --green: #56a81c;
    --text-grey: #4d4d4d;
    --dots: #8a8a8a;
  }
  * { margin: 0; padding: 0; box-sizing: border-box; }
  html, body {
    width: 1105px; height: 1200px; overflow: hidden;
    background: var(--backdrop);
    font-family: "Open Sans", Arial, sans-serif;
  }
  .card {
    position: absolute; left: 193px; width: 720px; height: 412px;
    background: var(--card); border-radius: 20px; overflow: hidden;
    box-shadow: 0 2px 6px rgba(0,0,0,0.18);
  }
  .card-front { top: 146px; }
  .card-back { top: 604px; }

  /* Front */
  .doctor-name {
    position: absolute; top: 28px; width: 100%; text-align: center;
    color: var(--navy); font-weight: 600; font-size: 26px;
  }
  .doctor-title {
    position: absolute; top: 63px; width: 100%; text-align: center;
    color: var(--green); font-weight: 600; font-size: 18px;
  }
  .practice-address, .practice-web {
    position: absolute; width: 100%; text-align: center;
    color: var(--text-grey); font-size: 19px;
  }
  .practice-address { top: 100px; }
  .practice-web { top: 132px; }
  .frames-art { position: absolute; left: 0; top: 168px; width: 720px; height: 220px; }

  /* Back */
  .brand {
    position: absolute; left: 36px; top: 96px;
    display: flex; align-items: center; gap: 10px;
  }
  .brand-dot { width: 18px; height: 18px; border-radius: 50%; background: var(--navy); }
  .brand-name { color: var(--navy); font-weight: 700; font-size: 24px; line-height: 1.2; }
  .appointment-heading {
    position: absolute; right: 53px; top: 36px;
    color: var(--navy); font-weight: 600; font-size: 27px;
  }
  .field { position: absolute; font-size: 19px; line-height: 1; }
  .field-line { position: absolute; border-bottom: 2px dotted var(--dots); height: 1px; }
  .label-grey { color: var(--text-grey); }
  .label-navy { color: var(--navy); font-size: 20px; }
  .ampm { color: var(--navy); font-size: 16px; }
  .cancel-note {
    position: absolute; top: 342px; width: 100%; text-align: center;
    color: var(--text-grey); font-style: italic; font-size: 15px; line-height: 20px;
  }
</style>
</head>
<body>

<section class="card card-front">
  <div class="doctor-name">Dr. Petra Lindqvist</div>
  <div class="doctor-title">Optometrist</div>
  <div class="practice-address">4172 S Corbell Ave, Alderhaven, OR 98736</div>
  <div class="practice-web">www.PMarlowvistaeyecare.example</div>
  <svg class="frames-art" viewBox="0 0 720 220" role="img" aria-label="Illustration of large blue eyeglass frames spanning the card">
    <defs>
      <linearGradient id="frameTone" x1="0" y1="0" x2="1" y2="0.4">
        <stop offset="0" stop-color="#8a96c8"/>
        <stop offset="0.45" stop-color="#3a4a95"/>
        <stop offset="1" stop-color="#1f2e78"/>
      </linearGradient>
    </defs>
    <path d="M0 0 C150 8 250 8 360 30 C470 8 570 8 720 0 L720 220 L0 220 Z" fill="url(#frameTone)"/>
  </svg>
</section>

<section class="card card-back">
  <div class="brand">
    <span class="brand-dot"></span>
    <span class="brand-name">Marlow Vista Eyecare</span>
  </div>
  <div class="appointment-heading">Next Appointment</div>

  <div class="field-line" style="left:43px; top:213px; width:418px;"></div>
  <div class="field label-grey" style="left:472px; top:197px;">has an appointment</div>

  <div class="field label-navy" style="left:35px; top:248px;">Date :</div>
  <div class="field-line" style="left:104px; top:265px; width:272px;"></div>
  <div class="field label-navy" style="left:399px; top:248px;">Time :</div>
  <div class="field-line" style="left:460px; top:265px; width:140px;"></div>
  <div class="field ampm" style="left:609px; top:253px;">AM/PM</div>

  <div class="field label-navy" style="left:35px; top:303px;">Date :</div>
  <div class="field-line" style="left:104px; top:320px; width:272px;"></div>
  <div class="field label-navy" style="left:399px; top:303px;">Time :</div>
  <div class="field-line" style="left:460px; top:320px; width:140px;"></div>
  <div class="field ampm" style="left:609px; top:308px;">AM/PM</div>

  <p class="cancel-note">Please give me 24 hours notice if you are unable to keep your appointment or<br>a cancellation fee may be charged.</p>
</section>

</body>
</html>
```